Dietary supplement, Clean and simple.

Hi,
I’d like to talk about the project,

About us:
We are a dietary supplement (Vitamins, Minerals, amino acids etc.) company.
The goal is to have about 25 products at the end of this year. However, for this goal to be achieved we need a good label design to make our products represent our company values.
I’ll be here every day supporting your questions, we are fully committed to making the highest/best quality/customer experience possible.

About the design and our values:
- Professional (We are in the industry of professionalism and expertise. I would love to show we are competent at this, Id. Like to have the labels looks like we have done our research.)
- Efficient (White spacing, good use of the space available.)
- Simple (Straight forward, in 5 seconds they have to know what the product they have is/how functions. We’re trying to simplify it for the consumer.
- No distractions (the only visually “distracting” factor can be the vector art.)

The guidelines:
The goal is to have a universal design, with one element that changes (Vector art). I’ll attach a file/multiple files I think can show some visuals on what I’m looking for, and what parts of the design I think are good/bad.

Label size: 69x155mm (Front is 77.5mm)

Design whatever you think fits our image. You’re the design expert, all I care about is that it fits our company standards/image.

Use this color/font.
Font: Sans Serif
Main company color is Mind green #237D62 (Use this color for something in the design.)

What I thought would be cool/might looks ugly, who knows:
1. The front of the label: Should have 1 vector art, preferably in the top right corner. (That looks good in multiple colors. The vector can have multiple areas to color, I would prefer 2 main colors in the vector art. The interchangeable colors are used for multiple kinds of products.)
2. Text/product information on the left. The text that will have to be displayed:
- Product name for instance “Magnesium + B6”
- Description for the product for instance “Magnesium with ginger taste”
- Company name or logo. (Add ® behind it. We are soon to be trademark registered.)
3. We need to show the "daily intake" amount on the front and also the amount in the complete bottle. For instance, “Daily intake 1 capsule, 60 capsules”.
• You don’t have to design the backside of the label. After I chose a design, I’d like to chat and give specific information on what areas need to be assigned where. (Too complex because of the law.)
Updates

Hi, Please make the deadline 31 days total. I want designers to have the time to design. And not be rushed to finish it.

I want to extend the deadline because i feel like a slightly more medical look would be interesting. Hope you can come up with something!!

Target Market(s)

Dietary supplement consumers

Industry/Entity Type

Dietary supplements

Font styles to use
Sans Serif

Colors

Designer to choose colors to be used in the design.

Requirements
Must have
• Trademark icon "®" has to be at the top right after the company logo(text of logo)/name.

```html
<!DOCTYPE html>
<html lang="en">
<head>
<meta charset="utf-8">
<title>Verdant Crest Magnesium B+ Label</title>
<link href="https://fonts.googleapis.com/css2?family=Montserrat:wght@400;500;700;800&display=swap" rel="stylesheet">
<style>
  :root {
    --page: #ffffff;
    --band: #e6e7e8;
    --navy: #062a52;
    --blue: #0a5fa3;
    --cyan: #08a9e6;
    --silver: #c9cbce;
    --gold-dark: #8a5a12;
    --gold: #e6b73a;
    --gold-light: #f5d77a;
    --mind-green: #237D62;
    --pill: #0e5a84;
    --white: #ffffff;
  }
  * { margin: 0; padding: 0; box-sizing: border-box; }
  html, body { width: 1200px; height: 534px; overflow: hidden; background: var(--page); }
  .label-canvas { position: relative; width: 1200px; height: 534px; font-family: 'Montserrat', sans-serif; }

  .wrap-band { position: absolute; left: 23px; top: 68px; width: 1149px; height: 398px; background: var(--band); border-radius: 34px; }

  .front-panel { position: absolute; left: 298px; top: 0; width: 599px; height: 534px; }
  .front-panel svg { display: block; }

  .brand { position: absolute; left: 700px; top: 96px; width: 160px; text-align: center; color: var(--mind-green); font-weight: 800; }
  .brand-name { position: relative; display: inline-block; font-size: 28px; letter-spacing: 0.5px; line-height: 1; }
  .brand-mark { position: absolute; right: -12px; top: -5px; font-size: 10px; }
  .brand-sub { font-size: 12px; letter-spacing: 8px; margin-top: 7px; padding-left: 8px; }

  .product-name { position: absolute; left: 421px; top: 268px; font-weight: 800; font-size: 48px; letter-spacing: 0.5px; line-height: 1;
    background: linear-gradient(180deg, #3fc1ea 0%, #0b6fae 55%, #063e73 100%);
    -webkit-background-clip: text; background-clip: text; color: transparent; }
  .variant-dot { position: absolute; left: 746px; top: 277px; width: 31px; height: 31px; border-radius: 50%;
    background: radial-gradient(circle at 40% 35%, #2cb6e8, var(--blue)); color: var(--white); font-weight: 700; font-size: 14px;
    display: flex; align-items: center; justify-content: center; }
  .product-desc { position: absolute; left: 420px; top: 317px; width: 355px; height: 17px; border-radius: 9px; background: var(--pill);
    color: var(--white); font-weight: 500; font-size: 17.5px; line-height: 17px; text-align: center; }

  .net-weight { position: absolute; left: 345px; top: 456px; width: 44px; height: 44px; border-radius: 50%; background: var(--white);
    color: var(--navy); text-align: center; font-weight: 800; }
  .net-weight .amount { display: block; font-size: 15px; line-height: 1; margin-top: 10px; }
  .net-weight .unit { display: block; font-size: 7px; font-weight: 700; }

  .dose-badge { position: absolute; left: 720px; top: 397px; width: 100px; height: 100px; border-radius: 50%;
    background: linear-gradient(160deg, var(--gold-light), var(--gold-dark) 55%, var(--gold)); padding: 4px; }
  .dose-inner { width: 100%; height: 100%; border-radius: 50%; overflow: hidden; background: var(--white); display: flex; flex-direction: column; }
  .dose-top { height: 46%; text-align: center; color: var(--navy); padding-top: 12px; }
  .dose-top .hint { display: block; font-size: 9.5px; font-weight: 400; line-height: 1; }
  .dose-top .daily { display: block; font-size: 12.5px; font-weight: 700; line-height: 1.2; margin-top: 2px; }
  .dose-bottom { flex: 1; background: var(--navy); color: var(--white); text-align: center; }
  .dose-bottom .count { display: block; font-size: 34px; font-weight: 800; line-height: 1; margin-top: 1px; }
  .dose-bottom .unit { display: block; font-size: 10px; font-weight: 700; line-height: 1; }
</style>
</head>
<body>
<main class="label-canvas">
  <div class="wrap-band"></div>

  <div class="front-panel">
    <svg width="599" height="534" viewBox="0 0 599 534" role="img" aria-label="Decorative background artwork in blue, silver and gold tones">
      <defs>
        <linearGradient id="panelTone" x1="1" y1="0" x2="0" y2="1">
          <stop offset="0" stop-color="#ffffff"/>
          <stop offset="0.25" stop-color="#eceded"/>
          <stop offset="0.5" stop-color="#c9cbce"/>
          <stop offset="0.72" stop-color="#3f86bd"/>
          <stop offset="1" stop-color="#062a52"/>
        </linearGradient>
      </defs>
      <path class="panel-base" d="M0 0 H599 V534 H0 C28 380 28 150 0 0 Z" fill="url(#panelTone)"/>
    </svg>
  </div>

  <div class="brand">
    <div class="brand-name">VERDANT<span class="brand-mark">®</span></div>
    <div class="brand-sub">CREST</div>
  </div>

  <h1 class="product-name">MAGNESIUM</h1>
  <div class="variant-dot">B+</div>
  <p class="product-desc">Magnesium with lemon taste</p>

  <div class="net-weight"><span class="amount">180</span><span class="unit">grams</span></div>

  <div class="dose-badge">
    <div class="dose-inner">
      <div class="dose-top"><span class="hint">take daily</span><span class="daily">1 CAPSULE</span></div>
      <div class="dose-bottom"><span class="count">60</span><span class="unit">capsules</span></div>
    </div>
  </div>
</main>
</body>
</html>
```